Business card based on your logo design "Marlowe&Co"

Can you please design a business card based on the logo artwork you designed for our business. Double sided as per your submitted image of possible application of logo.

```html
<!DOCTYPE html>
<html lang="en">
<head>
<meta charset="utf-8">
<title>Marlowe&amp;Co – Business Card</title>
<link rel="stylesheet" href="https://fonts.googleapis.com/css2?family=Oswald:wght@500&family=Quicksand:wght@600&family=Arimo:wght@400;700&display=swap">
<style>
  :root {
    --ink: #333333;
    --orange: #f7941d;
    --paper: #ffffff;
    --text: #2b2b2b;
  }
  html, body {
    margin: 0;
    padding: 0;
    width: 1200px;
    height: 404px;
    overflow: hidden;
    background: var(--paper);
  }
  .canvas {
    position: relative;
    width: 1200px;
    height: 404px;
  }
  .card-front {
    position: absolute;
    left: 0; top: 0;
    width: 600px; height: 404px;
    background: var(--paper);
  }
  .card-back {
    position: absolute;
    left: 642px; top: 28px;
    width: 541px; height: 357px;
    background: var(--ink);
  }
  .wordmark {
    position: absolute;
    overflow: visible;
  }
  .wordmark-name { font-family: 'Oswald', sans-serif; font-weight: 500; }
  .wordmark-tagline { font-family: 'Quicksand', sans-serif; font-weight: 600; }
  .name-bar {
    position: absolute;
    left: 18px; top: 250px;
    width: 543px; height: 35px;
    background: var(--ink);
    color: var(--paper);
    font-family: 'Arimo', sans-serif;
    font-size: 16px;
    font-weight: 700;
    display: flex;
    align-items: center;
    justify-content: center;
    gap: 5px;
  }
  .name-bar .role { font-weight: 400; font-size: 13px; }
  .contact {
    position: absolute;
    display: flex;
    align-items: center;
    gap: 10px;
    font-family: 'Arimo', sans-serif;
    font-size: 16px;
    color: var(--text);
    white-space: nowrap;
  }
  .contact svg { width: 16px; height: 16px; fill: var(--orange); flex: none; }
</style>
</head>
<body>
<div class="canvas">

  <section class="card-front">
    <svg class="wordmark" style="left:0;top:0" width="600" height="240" viewBox="0 0 600 240">
      <text class="wordmark-name" x="20" y="194" font-size="160" fill="var(--ink)" textLength="541" lengthAdjust="spacingAndGlyphs">MARLOWE&amp;CO</text>
      <rect x="20" y="203" width="540" height="2" fill="var(--orange)"/>
      <text class="wordmark-tagline" x="21" y="228" font-size="19" fill="var(--ink)" textLength="536" lengthAdjust="spacing">Building and Project Management</text>
    </svg>

    <div class="name-bar"><span class="person">Dean R. Holt</span><span class="role">CEO</span></div>

    <div class="contact" style="left:92px;top:299px">
      <svg viewBox="0 0 16 16"><path d="M3.6 1l2.6 3.1-1.5 1.6c.9 2 2.6 3.7 4.6 4.6l1.6-1.5 3.1 2.6-1.4 2.4C7 13.8 2.2 9 1.2 2.4z"/></svg>
      <span>414-555-0182</span>
    </div>
    <div class="contact" style="left:92px;top:326px">
      <svg viewBox="0 0 16 16"><rect x="4" y="1" width="8" height="4"/><rect x="1" y="6" width="14" height="6" rx="1"/><rect x="4" y="10" width="8" height="5"/></svg>
      <span>414-555-0183</span>
    </div>
    <div class="contact" style="left:271px;top:299px">
      <svg viewBox="0 0 16 16"><path d="M1 3h14v10H1z"/><path d="M1 3l7 6 7-6" fill="none" stroke="#fff" stroke-width="1.3"/></svg>
      <span>DeanRHolt@marloweco.com</span>
    </div>
    <div class="contact" style="left:271px;top:326px">
      <svg viewBox="0 0 16 16"><circle cx="8" cy="8" r="7"/><path d="M1 8h14M8 1c-3 3.5-3 10.5 0 14M8 1c3 3.5 3 10.5 0 14" fill="none" stroke="#fff" stroke-width="1"/></svg>
      <span>www.marloweco.com</span>
    </div>
    <div class="contact" style="left:106px;top:361px">
      <svg viewBox="0 0 16 16"><path d="M8 0.5a5.5 5.5 0 0 0-5.5 5.5C2.5 10 8 15.5 8 15.5S13.5 10 13.5 6A5.5 5.5 0 0 0 8 .5zm0 3.3a2.2 2.2 0 1 1 0 4.4 2.2 2.2 0 0 1 0-4.4z"/></svg>
      <span>2318 Cedar Hollow Road Brookfield, WI 53045</span>
    </div>
  </section>

  <section class="card-back">
    <svg class="wordmark" style="left:0;top:0" width="541" height="357" viewBox="0 0 541 357">
      <text class="wordmark-name" x="93" y="217" font-size="93" fill="var(--paper)" textLength="358" lengthAdjust="spacingAndGlyphs">MARLOWE&amp;CO</text>
      <rect x="93" y="227" width="357" height="1.5" fill="var(--paper)"/>
      <text class="wordmark-tagline" x="94" y="244" font-size="13" fill="var(--paper)" textLength="354" lengthAdjust="spacing">Building and Project Management</text>
    </svg>
  </section>

</div>
</body>
</html>
```